Lanterns At Dusk (Tattoo Shop)

its for a business sign that is 8 foot by 22 inches looking for a classy modern black and white (Maybe some gold) easy to read sign. As you can see there is some very poor boarders added, please add what you think will look good. ITs for a tattoo shop. Maybe shoot one or two of the desgins with a fillagree look, still keeping it simple.

Target Market(s)

beginner and veteran tattoo collectors, leaving behind the old back door biker shop and stepping into the new age of tattooing. Looking to attract all types and make clients feel comfortable getting large pieces

Industry/Entity Type

Tattoo

Logo Text

Lanterns At Dusk

Font styles to use
Decorative
Other font styles liked:
• Modern

Colors
000000
959595
eaeaea
d3d3d3
ffffff

Requirements
Must have
• Lanterns At Dusk (words), using as much space as you can. Be black and white in color and a few samples in gold. Have the proper dimension easily legible. Some boarders.
Nice to have
• using the number of designs wisely if you think of something that will look good feel free to add it. Adding a few sample for shades of grey only color I would want added is gold ( fairly certain on black and white but I would like to see one or tow with gold)
• Maybe one example of decorative

```html
<!DOCTYPE html>
<html lang="en">
<head>
<meta charset="utf-8">
<title>Lanterns At Dusk — Shop Sign</title>
<link rel="stylesheet" href="https://fonts.googleapis.com/css2?family=Josefin+Sans:wght@400&display=swap">
<style>
  :root {
    --sign-black: #1f1e1c;
    --sign-white: #ffffff;
    --ornament-grey: #d3d3d3;
  }
  html, body {
    margin: 0;
    padding: 0;
    width: 1200px;
    height: 276px;
    overflow: hidden;
    background: var(--sign-black);
  }
  .sign {
    position: relative;
    box-sizing: border-box;
    width: 1200px;
    height: 276px;
    padding: 30px 60px 22px;
    background: var(--sign-black);
    overflow: hidden;
    display: flex;
    flex-direction: column;
    align-items: center;
    justify-content: center;
    font-family: "Josefin Sans", sans-serif;
    font-weight: 400;
    color: var(--sign-white);
    text-transform: uppercase;
  }
  .sign__name {
    margin: 0;
    font-size: 168px;
    line-height: 0.9;
    letter-spacing: 18px;
    padding-left: 18px;
    white-space: nowrap;
  }
  .sign__tagline {
    margin: 14px 0 0;
    font-size: 40px;
    line-height: 1;
    letter-spacing: 8px;
    padding-left: 8px;
    white-space: nowrap;
  }
  .corner-ornament {
    position: absolute;
    width: 30px;
    height: 30px;
    background: var(--ornament-grey);
    opacity: 0.85;
  }
  .corner-ornament--tl { top: 4px; left: 4px; }
  .corner-ornament--tr { top: 4px; right: 4px; }
  .corner-ornament--bl { bottom: 4px; left: 4px; }
  .corner-ornament--br { bottom: 4px; right: 4px; }
</style>
</head>
<body>
<div class="sign">
  <h1 class="sign__name">Lanterns</h1>
  <p class="sign__tagline">At Dusk</p>
  <div class="corner-ornament corner-ornament--tl" role="img" aria-label="Filigree corner ornament"></div>
  <div class="corner-ornament corner-ornament--tr" role="img" aria-label="Filigree corner ornament"></div>
  <div class="corner-ornament corner-ornament--bl" role="img" aria-label="Filigree corner ornament"></div>
  <div class="corner-ornament corner-ornament--br" role="img" aria-label="Filigree corner ornament"></div>
</div>
</body>
</html>
```